Linen Sparrow- Hand made fashion accessories

Linen sparrow is a new business that will be selling hand made fashion accessories for women such as bags, baskets, knecklaces etc. The items are all hand made from Africa. I would like natural colors leaning more to the cardboard rustic look. I would like the card to look simple but elegant at the same time.

Industry/Entity Type

Business

Contact Information for Business Card

www.linensparrow-example.com.au
sales@linensparrow-example.com.au
Tel: 0427586302

Font styles to use
Decorative
Script

Requirements
Must have
• Earthy and rustic colours. Straw, cardboard etc. Fine black cursive print. One side of card only name
• second side website, email and tel.
Should not have
• No need to have any description of what business sells or does. No pictures of anything.

```html
<!DOCTYPE html>
<html lang="en">
<head>
<meta charset="utf-8">
<title>Linen Sparrow – Business Card</title>
<link href="https://fonts.googleapis.com/css2?family=Great+Vibes&family=Cormorant+Garamond:wght@500;600&display=swap" rel="stylesheet">
<style>
  :root {
    --kraft: #c8a676;
    --kraft-deep: #a9834f;
    --straw: #e4cb8d;
    --straw-light: #efdcae;
    --bark: #6b4a2b;
    --bark-deep: #4a3220;
    --ink: #1b1410;
    --line: #f6ecd6;
    --page: #ffffff;
  }
  * { margin: 0; padding: 0; box-sizing: border-box; }
  html, body {
    width: 1163px;
    height: 1200px;
    overflow: hidden;
    background: var(--page);
    font-family: "Cormorant Garamond", Georgia, serif;
  }
  .canvas { position: relative; width: 1163px; height: 1200px; }
  .card-art { position: absolute; left: 0; top: 0; }
  .card-face { fill: var(--kraft); }
  .straw-band { fill: var(--straw); }
  .top-tab { fill: var(--straw); stroke: var(--line); stroke-width: 3; }
  .contact-panel { fill: var(--kraft); stroke: var(--line); stroke-width: 3; }

  .brand-name {
    position: absolute;
    color: var(--ink);
    font-family: "Great Vibes", cursive;
    font-weight: 400;
    line-height: 1.2;
    white-space: nowrap;
  }
  .brand-name--front { left: 118px; top: 240px; font-size: 104px; }
  .brand-name--back { left: 200px; top: 700px; font-size: 96px; }

  .contact {
    position: absolute;
    display: flex;
    align-items: center;
    gap: 18px;
    color: var(--ink);
    font-size: 23px;
    font-weight: 600;
    letter-spacing: 0.3px;
    white-space: nowrap;
  }
  .contact svg { flex: none; }
  .contact--phone { left: 164px; top: 982px; }
  .contact--email { left: 164px; top: 1061px; }
  .contact--web { left: 640px; top: 1061px; }
</style>
</head>
<body>
<div class="canvas">
  <svg class="card-art" width="1163" height="1200" viewBox="0 0 1163 1200" xmlns="http://www.w3.org/2000/svg">
    <defs>
      <linearGradient id="splash-tones" x1="0" y1="0" x2="1" y2="1">
        <stop offset="0" stop-color="#e4cb8d"/>
        <stop offset="0.55" stop-color="#b8915c"/>
        <stop offset="1" stop-color="#6b4a2b"/>
      </linearGradient>
      <linearGradient id="faint-vine" x1="0" y1="0" x2="1" y2="1">
        <stop offset="0" stop-color="#f6ecd6" stop-opacity="0.18"/>
        <stop offset="1" stop-color="#f6ecd6" stop-opacity="0.30"/>
      </linearGradient>
      <linearGradient id="notch-tone" x1="0" y1="0" x2="0" y2="1">
        <stop offset="0" stop-color="#8a6238"/>
        <stop offset="1" stop-color="#4a3220"/>
      </linearGradient>
      <linearGradient id="panel-shade" x1="0" y1="0" x2="0" y2="1">
        <stop offset="0" stop-color="#4a3220" stop-opacity="0"/>
        <stop offset="1" stop-color="#4a3220" stop-opacity="0.35"/>
      </linearGradient>
    </defs>

    <g class="card-front">
      <rect class="card-face" x="94" y="0" width="965" height="548"/>
      <rect class="splash-art" role="img" aria-label="Straw and bark toned paint splash with pale leafy vines"
            x="660" y="0" width="399" height="300" rx="110" fill="url(#splash-tones)" opacity="0.85"/>
    </g>

    <g class="card-back">
      <rect class="card-face" x="94" y="580" width="965" height="552"/>
      <rect class="straw-band" x="94" y="580" width="965" height="19"/>
      <polygon class="top-tab" points="551,598 575,637 935,637 957,598"/>
      <rect class="vine-art" role="img" aria-label="Faint pale leafy vine decoration"
            x="720" y="660" width="339" height="380" rx="60" fill="url(#faint-vine)"/>
      <rect x="94" y="880" width="965" height="60" fill="url(#panel-shade)"/>
      <rect class="notch-glow" x="565" y="920" width="378" height="80" rx="16" fill="url(#notch-tone)"/>
      <polygon class="contact-panel" points="94,940 551,940 580,998 928,998 957,940 1059,940 1059,1131 94,1131"/>
    </g>
  </svg>

  <div class="brand-name brand-name--front">Linen Sparrow</div>
  <div class="brand-name brand-name--back">Linen Sparrow</div>

  <div class="contact contact--phone">
    <svg width="22" height="26" viewBox="0 0 22 26" aria-hidden="true">
      <path d="M5 1 L9 7 L6 10 C7 14 9 17 13 19 L16 16 L21 21 L18 25 C9 24 2 15 1 5 Z" fill="none" stroke="#1b1410" stroke-width="2"/>
    </svg>
    <span>0427586302</span>
  </div>
  <div class="contact contact--email">
    <svg width="26" height="18" viewBox="0 0 26 18" aria-hidden="true">
      <rect x="1" y="1" width="24" height="16" fill="#1b1410"/>
      <path d="M1 1 L13 10 L25 1" fill="none" stroke="#c8a676" stroke-width="2"/>
    </svg>
    <span>sales@linensparrow-example.com.au</span>
  </div>
  <div class="contact contact--web">
    <svg width="24" height="24" viewBox="0 0 24 24" aria-hidden="true">
      <circle cx="12" cy="12" r="10.5" fill="none" stroke="#1b1410" stroke-width="2"/>
      <ellipse cx="12" cy="12" rx="4.5" ry="10.5" fill="none" stroke="#1b1410" stroke-width="1.6"/>
      <line x1="1.5" y1="12" x2="22.5" y2="12" stroke="#1b1410" stroke-width="1.6"/>
      <line x1="3.5" y1="6.5" x2="20.5" y2="6.5" stroke="#1b1410" stroke-width="1.4"/>
      <line x1="3.5" y1="17.5" x2="20.5" y2="17.5" stroke="#1b1410" stroke-width="1.4"/>
    </svg>
    <span>www.linensparrow-example.com.au</span>
  </div>
</div>
</body>
</html>
```